I challenge you to create Denmark's coolest roofing company website

We need to have a website created for our roofing company.

I have some pages that can be used as a starting point because there are some things we would like to have, one important thing is a roof calculator, in addition to that information about the company, pictures of tasks we have completed, links to Chatterbox and Snapwhirl pages.

reviews from rovly, etc. should also be visible on the page.

we have lots of pictures, videos, logos,

we need to have a nice home page that is just a little cooler than the competitors.
we need to steal their customer. the page should be easy and clear but with a nice design.
an important thing is the calculator.
come up with some suggestions we are quite open as long as it is a nice design
Updates

I have made an update in the PDF file with some thoughts and wishes. The file has been uploaded.

Target Market(s)

20-60

Industry/Entity Type

carpenter - roofer

Coding

Coded - Design and coding required

Number of Pages Required

4 page

Font styles to use
Sans Serif

Colors
EB3D1F
EC4F4E
F09395
F8D3D4
FCEDEE

Requirements
Must have
• Roof calculator, nice design, easy to get around
Nice to have
• the competitors : https://bolvernhusmesteren.dk https://kilde-lys.dk https://fernmolhusvaerk.dk

```html
<!DOCTYPE html>
<html lang="en">
<head>
<meta charset="utf-8">
<title>Roofing Company – Home</title>
<link href="https://fonts.googleapis.com/css2?family=Russo+One&family=Poppins:wght@400;500;600&display=swap" rel="stylesheet">
<style>
:root{
  --red:#EB3D1F;
  --red-soft:#EC4F4E;
  --pink:#F09395;
  --blush:#F8D3D4;
  --mist:#FCEDEE;
  --ink:#121212;
  --dark:#161616;
  --text:#333;
  --muted:#666;
  --light:#eeeeee;
  --white:#fff;
}
*{box-sizing:border-box;margin:0;padding:0}
html,body{width:1200px;height:4918px;overflow:hidden}
body{position:relative;background:var(--white);font-family:"Poppins",sans-serif;color:var(--text)}
.abs{position:absolute}
.display{font-family:"Russo One",sans-serif;color:var(--ink);text-transform:uppercase;letter-spacing:1px}
.photo{position:absolute}
a{color:inherit;text-decoration:none}

/* header */
.topbar{left:560px;top:0;width:640px;height:33px;background:var(--ink);clip-path:polygon(20px 0,100% 0,100% 100%,0 100%);display:flex;align-items:center;padding-left:44px;gap:34px;font-size:11px;color:#fff}
.topbar .ico{color:var(--red);margin-right:6px}
.topbar .social{margin-left:auto;margin-right:26px;display:flex;gap:10px;font-size:10px;color:var(--red)}
.logo{left:88px;top:40px;font-family:"Russo One",sans-serif;font-size:32px;color:var(--ink);letter-spacing:1px}
.nav{left:434px;top:60px;display:flex;gap:22px;font-size:11px;font-weight:500;color:var(--ink);text-transform:uppercase}
.nav .active{color:var(--red);border-bottom:2px solid var(--red);padding-bottom:3px}
.btn{display:inline-flex;align-items:center;justify-content:center;font-size:11px;font-weight:500;text-transform:uppercase;color:#fff;background:var(--red)}
.quote-btn{left:954px;top:50px;width:156px;height:38px}

/* hero */
.hero-photo{left:0;top:103px;width:1200px;height:810px;background:linear-gradient(120deg,#5d6670 0%,#3f4449 40%,#2b2a28 70%,#6a5a46 100%)}
.hero-title{left:90px;top:336px;font-size:46px;line-height:54px;color:#fff}
.hero-sub{left:90px;top:462px;font-size:13px;color:#fff}
.hero-btn1{left:90px;top:506px;width:180px;height:40px}
.hero-btn2{left:279px;top:506px;width:170px;height:40px;background:transparent;border:1px solid #fff}
.promise{left:752px;top:506px;width:351px;height:353px;background:var(--red);text-align:center;color:#fff;padding:56px 46px 0}
.promise .eyebrow{font-size:13px;text-transform:uppercase}
.promise h2{font-family:"Russo One",sans-serif;font-size:23px;line-height:29px;margin-top:26px;text-transform:uppercase;letter-spacing:1px}
.promise p{font-size:13px;margin-top:18px;line-height:20px;color:var(--mist)}

/* why */
.why-title{left:628px;top:980px;font-size:28px;line-height:34px}
.why-text{left:628px;top:1070px;width:400px;font-size:12px;line-height:20px;color:var(--muted)}
.why-list{left:628px;top:1170px;list-style:none;font-size:12px;color:var(--ink)}
.why-list li{height:34px;display:flex;align-items:center}
.why-list li::before{content:"";width:7px;height:7px;background:var(--red);transform:rotate(45deg);margin-right:11px}
.why-list b{font-weight:600;margin-right:4px}

/* calculator */
.calc-title{left:118px;top:1550px;font-size:28px;line-height:34px}
.calc-text{left:118px;top:1636px;width:430px;font-size:12px;line-height:20px;color:var(--muted)}
.field{height:37px;width:189px;background:#eeeeee;font-size:10px;color:#777;display:flex;align-items:center;padding:0 20px;justify-content:space-between}
.field .chev{color:var(--red);font-size:12px}
.calc-link{left:118px;top:1803px;font-size:12px;color:var(--red);text-decoration:underline;text-transform:uppercase}
.dots{left:900px;top:1416px;width:62px;height:104px;background-image:radial-gradient(var(--ink) 1.6px,transparent 1.8px);background-size:10px 10px}

/* services */
.services-bg{left:0;top:1965px;width:1200px;height:560px}
.services-title{left:0;width:1200px;top:2120px;text-align:center;font-size:28px;color:#fff}
.card{position:absolute;top:2187px;width:246px;height:390px;background:#fff;clip-path:polygon(0 0,100% 0,100% 92%,0 100%);box-shadow:0 10px 20px rgba(0,0,0,.1)}
.card .pic{height:204px}
.card h3{font-family:"Russo One",sans-serif;font-size:11px;color:var(--ink);text-transform:uppercase;margin:28px 28px 0}
.card p{font-size:10px;line-height:16px;color:var(--muted);margin:12px 28px 0}
.card a{display:inline-block;font-size:10px;color:var(--red);text-decoration:underline;margin:10px 28px 0;text-transform:uppercase}

/* testimonials */
.testi-title{left:132px;top:2690px;font-size:28px}
.testi-sub{left:132px;top:2732px;font-size:12px;color:var(--muted)}
.arrow{position:absolute;width:44px;height:44px;display:flex;align-items:center;justify-content:center;color:#fff;font-size:16px}
.arrow.dark{background:var(--ink)}
.arrow.red{background:var(--red)}
.review{position:absolute;top:2815px;width:260px}
.review .mark{font-family:"Russo One",sans-serif;font-size:64px;color:var(--red);line-height:50px;height:44px}
.review p{font-size:12px;line-height:20px;color:var(--muted);margin-top:18px;height:86px}
.review .who{display:flex;justify-content:space-between;align-items:center;margin-top:24px}
.review .name{font-family:"Russo One",sans-serif;font-size:15px;color:var(--ink)}
.review .stars{color:#f0a028;font-size:14px;letter-spacing:3px}
.divider{position:absolute;top:2795px;width:1px;height:220px;background:#ddd}

/* projects */
.projects-bg{left:0;top:3081px;width:1200px;height:602px;background:var(--light)}
.projects-title{left:0;width:1200px;top:3146px;text-align:center;font-size:28px}
.project{position:absolute;top:3211px;height:338px}
.project .cap{position:absolute;left:38px;bottom:40px;color:#fff}
.project h3{font-family:"Russo One",sans-serif;font-size:15px;text-transform:uppercase}
.project p{font-size:11px;line-height:18px;margin-top:10px;width:380px}

/* contact */
.contact-title{left:675px;top:3780px;font-size:28px}
.contact-text{left:675px;top:3828px;width:390px;font-size:12px;line-height:20px;color:var(--muted)}
.input{position:absolute;height:34px;border-bottom:1px solid #ddd;font-size:12px;color:#888;padding-left:12px;display:flex;align-items:center}
.send{left:675px;top:4058px;width:180px;height:38px}

/* footer */
.footer-logo{left:118px;top:4510px;font-family:"Russo One",sans-serif;font-size:50px;color:#fff;letter-spacing:1px}
.contact-pill{position:absolute;top:4506px;display:flex;align-items:center;gap:14px;color:#fff}
.contact-pill .sq{width:52px;height:52px;background:var(--red);display:flex;align-items:center;justify-content:center}
.contact-pill small{display:block;font-family:"Russo One",sans-serif;font-size:10px;text-transform:uppercase}
.contact-pill strong{display:block;font-family:"Russo One",sans-serif;font-size:21px;font-weight:400;text-transform:uppercase}
.f-social{left:118px;top:4670px;display:flex;gap:10px}
.f-social span{height:36px;padding:0 8px;border:1px solid #555;color:#ccc;font-size:9px;display:flex;align-items:center}
.copy{left:118px;top:4726px;font-size:11px;color:#ccc}
.f-col{position:absolute;top:4666px;color:#ddd}
.f-col h4{font-family:"Russo One",sans-serif;font-weight:400;font-size:14px;color:#fff;text-transform:uppercase;line-height:19px}
.f-col ul{list-style:none;margin-top:14px;font-size:11px;line-height:27px}
.newsletter{margin-top:18px;width:260px;border-bottom:1px solid #666;height:32px;display:flex;justify-content:space-between;align-items:center;font-size:11px}
.totop{left:1116px;top:4805px;width:44px;height:44px;background:var(--red);color:#fff;display:flex;align-items:center;justify-content:center;font-size:16px}
</style>
</head>
<body>

<!-- header -->
<div class="abs topbar">
  <span><span class="ico">✆</span>Call us - (012) 345-6789</span>
  <span><span class="ico">✉</span>info@example.com</span>
  <span class="social"><span>Chatterbox</span><span>Workweave</span><span>Snapwhirl</span></span>
</div>
<div class="abs logo">LOGO HERE</div>
<nav class="abs nav">
  <a class="active">Home</a><a>Services</a><a>Projects</a><a>Roof Calculator</a><a>About Us</a><a>Contact</a>
</nav>
<a class="abs btn quote-btn">Get a Free Quote</a>

<!-- hero -->
<div class="photo hero-photo" role="img" aria-label="Roofer in a hard hat and safety vest working with a drill on a tiled roof"></div>
<svg class="abs" style="left:0;top:690px" width="1200" height="240" viewBox="0 690 1200 240">
  <polygon points="0,862 790,705 1200,880 1200,930 0,930" fill="var(--red)"/>
  <polygon points="0,902 790,742 1200,906 1200,930 0,930" fill="var(--white)"/>
</svg>
<h1 class="abs display hero-title">Your Dream Roof,<br>Our Expert Care</h1>
<p class="abs hero-sub">Fast, Reliable and Affordable Roofing Services — 4–5 Months to Complete</p>
<a class="abs btn hero-btn1">Estimate Your Roof</a>
<a class="abs btn hero-btn2">View Our Projects</a>
<div class="abs promise">
  <div class="eyebrow">The Roofing Promise</div>
  <h2>Discover the ultimate peace of mind with our premium-quality roofing solutions.</h2>
  <p>Delivering unmatched durability, beauty, and value.</p>
</div>

<!-- why us -->
<svg class="abs" style="left:168px;top:897px" width="386" height="470">
  <polygon points="0,420 250,410 386,470 386,400 0,400" fill="var(--red)"/>
</svg>
<div class="photo" style="left:168px;top:897px;width:386px;height:467px;clip-path:polygon(0 14%,100% 0,100% 100%,75% 84%,0 92%);background:linear-gradient(160deg,#c9ced4,#4d5560 60%,#2f343a)" role="img" aria-label="Roofer kneeling on a dark metal roof fitting panels"></div>
<h2 class="abs display why-title">Why Our Roofing<br>Services Are the Best</h2>
<p class="abs why-text">Our company has over 20 years of experience in residential and commercial roofing. We use modern techniques and high-quality materials to ensure your roof is both durable and stylish. Our team is professional, friendly, and fully insured.</p>
<ul class="abs why-list">
  <li><b>Fast &amp; Reliable:</b> Complete your roof in just 4–5 months</li>
  <li><b>Expert Team:</b> Skilled carpenters and roofers</li>
  <li><b>High-Quality Materials:</b> Long-lasting roofs</li>
  <li><b>Customer Satisfaction:</b> Positive reviews from satisfied clients</li>
</ul>

<!-- calculator -->
<h2 class="abs display calc-title">Calculate Your<br>Roof Estimate Instantly</h2>
<p class="abs calc-text">Use our simple roof calculator to get a quick and accurate estimate. Know your roof cost before scheduling a visit.</p>
<div class="abs field" style="left:118px;top:1696px">Flat / Sloped / Gabled<span class="chev">⌄</span></div>
<div class="abs field" style="left:315px;top:1696px">Enter area in sq. ft. or meters</div>
<div class="abs field" style="left:118px;top:1740px">Tiles / Shingles / Metal<span class="chev">⌄</span></div>
<div class="abs field" style="left:315px;top:1740px;justify-content:flex-start;gap:8px"><span style="width:8px;height:8px;border:1px solid var(--red)"></span>Insulation, Waterproofing</div>
<a class="abs calc-link">Calculate My Roof Cost</a>

<!-- services -->
<svg class="abs services-bg" width="1200" height="610" viewBox="0 1965 1200 610">
  <polygon points="0,1965 1200,1965 1200,2455 0,2455" fill="var(--dark)"/>
  <polygon points="0,2400 340,2360 340,2420 0,2450" fill="var(--red)"/>
  <polygon points="0,2455 1200,2455 1200,2510 1100,2470" fill="var(--white)"/>
  <polygon points="880,2420 1200,2520 1200,2575 860,2440" fill="var(--dark)"/>
</svg>
<div class="dots abs"></div>
<div class="photo" style="left:645px;top:1467px;width:435px;height:565px;background:linear-gradient(150deg,#8a6d55,#5a4a3d 45%,#2f3b4c);box-shadow:0 10px 30px rgba(0,0,0,.2)" role="img" aria-label="Roofer in an orange hard hat measuring a gutter with a tape measure"></div>
<div class="photo" style="left:914px;top:1767px;width:246px;height:181px;border:3px solid #fff;background:linear-gradient(140deg,#9aa0a6,#50575f)" role="img" aria-label="Worker in a white hard hat installing roof panels"></div>
<h2 class="abs display services-title">Our Roofing Services</h2>
<div class="card" style="left:92px"><div class="pic" style="background:linear-gradient(170deg,#b9bec4,#444b52)" role="img" aria-label="Roofer on a residential metal roof"></div><h3>Residential Roofing</h3><p>High-quality roofs designed for homes of all sizes. Durable, stylish, and built to last, ensuring…</p><a>Learn More</a></div>
<div class="card" style="left:347px"><div class="pic" style="background:linear-gradient(170deg,#56704a,#1f3a5e)" role="img" aria-label="Aerial view of a blue commercial building roof"></div><h3>Commercial Roofing</h3><p>Reliable roofing solutions for offices, warehouses, and commercial buildings. Engineered…</p><a>Learn More</a></div>
<div class="card" style="left:605px"><div class="pic" style="background:linear-gradient(170deg,#7a95b0,#7a4f3a)" role="img" aria-label="Roofers repairing a tiled roof"></div><h3>Roof Repairs &amp; Maintenance</h3><p>Fast, professional repairs and preventive maintenance to extend the life of your roof. We fix leaks…</p><a>Learn More</a></div>
<div class="card" style="left:862px"><div class="pic" style="background:linear-gradient(170deg,#8aa9c8,#5b4a40)" role="img" aria-label="Workers on the gable of a house roof"></div><h3>Custom Roofing Solutions</h3><p>Tailored roofing designs for unique structures or special requirements. From materials to style…</p><a>Learn More</a></div>

<!-- testimonials -->
<h2 class="abs display testi-title">What Our Clients Say</h2>
<p class="abs testi-sub">Real feedback from homeowners and businesses who trusted us with their roofing projects.</p>
<div class="arrow dark" style="left:969px;top:2698px">‹</div>
<div class="arrow red" style="left:1023px;top:2698px">›</div>
<div class="review" style="left:132px"><div class="mark">“</div><p>Excellent service! My new roof looks amazing and was completed quickly. The team was professional and kept me informed every step of the way.</p><div class="who"><span class="name">MAREN K.</span><span class="stars">★★★★★</span></div></div>
<div class="divider" style="left:429px"></div>
<div class="review" style="left:467px"><div class="mark">“</div><p>Professional team, high-quality materials, very satisfied with the results. Our office roof has never looked better!</p><div class="who"><span class="name">MAREN K.</span><span class="stars">★★★★★</span></div></div>
<div class="divider" style="left:767px"></div>
<div class="review" style="left:803px"><div class="mark">“</div><p>Highly recommend! They delivered exactly what they promised, on time and on budget. Truly a reliable roofing company.</p><div class="who"><span class="name">DITTE L.</span><span class="stars">★★★★★</span></div></div>

<!-- projects -->
<div class="abs projects-bg"></div>
<h2 class="abs display projects-title">Our Completed Projects</h2>
<div class="project" style="left:120px;width:471px;background:linear-gradient(160deg,#6f6a60,#2e2a26)" role="img" aria-label="Family in front of their home with a new asphalt shingle roof">
  <div class="cap"><h3>Modern Family Home – Austin, TX</h3><p>This residential roofing project featured a custom asphalt shingle system designed for durability and curb appeal.</p></div>
</div>
<div class="project" style="left:609px;width:471px;background:linear-gradient(160deg,#5e7fa6,#2a3442)" role="img" aria-label="Modern office building with a metal roof against glass towers">
  <div class="cap"><h3>Commercial Office Building – Dallas, TX</h3><p>A complete metal roofing installation for a 10,000 sq. ft. commercial property. The new roof provides superior…</p></div>
</div>
<div class="project" style="left:1097px;width:103px;overflow:hidden;background:linear-gradient(160deg,#6b6a5a,#2f2c24)" role="img" aria-label="Classic stone house with a restored roof">
  <div class="cap" style="left:36px;width:200px"><h3>Classic</h3><p style="width:200px">This project restoring the</p></div>
</div>
<div class="arrow dark" style="left:549px;top:3583px">‹</div>
<div class="arrow red" style="left:605px;top:3583px">›</div>

<!-- contact -->
<div class="photo" style="left:137px;top:3740px;width:474px;height:400px;background:linear-gradient(160deg,#3d4a3a,#6a5440 60%,#8b6a4b);box-shadow:0 10px 30px rgba(0,0,0,.15)" role="img" aria-label="Two roofers in white hard hats sitting on steps with coffee"></div>
<h2 class="abs display contact-title">Get in Touch With Us</h2>
<p class="abs contact-text">Have questions or want a free quote? Contact our team and we'll guide you every step of the way.</p>
<div class="input" style="left:675px;top:3890px;width:190px">First Name*</div>
<div class="input" style="left:880px;top:3890px;width:180px">Last Name*</div>
<div class="input" style="left:675px;top:3937px;width:190px">Email Address*</div>
<div class="input" style="left:880px;top:3937px;width:180px">Phone Number*</div>
<div class="input" style="left:675px;top:3984px;width:385px">Message*</div>
<a class="abs btn send">Estimate Your Roof</a>

<!-- footer -->
<svg class="abs" style="left:0;top:4230px" width="1200" height="688" viewBox="0 4230 1200 688">
  <polygon points="0,4395 790,4235 1200,4385 1200,4440 790,4260 0,4440" fill="var(--red)"/>
  <polygon points="0,4440 790,4260 1200,4440 1200,4918 0,4918" fill="var(--ink)"/>
</svg>
<div class="abs footer-logo">LOGO HERE</div>
<div class="contact-pill" style="left:536px">
  <div class="sq"><svg width="20" height="20" viewBox="0 0 24 24"><path d="M6.6 10.8a15 15 0 0 0 6.6 6.6l2.2-2.2a1 1 0 0 1 1-.25 11 11 0 0 0 3.6.6 1 1 0 0 1 1 1V20a1 1 0 0 1-1 1A17 17 0 0 1 3 4a1 1 0 0 1 1-1h3.5a1 1 0 0 1 1 1 11 11 0 0 0 .6 3.6 1 1 0 0 1-.25 1z" fill="#fff"/></svg></div>
  <div><small>Call us now</small><strong>012.345.6789</strong></div>
</div>
<div class="contact-pill" style="left:803px">
  <div class="sq"><svg width="22" height="18" viewBox="0 0 22 18"><rect x="1" y="1" width="20" height="16" fill="#fff"/><path d="M1 1l10 8 10-8" stroke="var(--red)" stroke-width="2" fill="none"/></svg></div>
  <div><small>Write to us</small><strong>info@example.com</strong></div>
</div>
<div class="abs f-social"><span>Chatterbox</span><span>Snapwhirl</span><span>Workweave</span></div>
<p class="abs copy">© 2025 — All Rights Reserved</p>
<div class="f-col" style="left:372px"><h4>Quick Links</h4><ul><li>Home</li><li>Services</li><li>Projects</li><li>Roof Calculator</li><li>About Us</li><li>Contact</li></ul></div>
<div class="f-col" style="left:553px"><h4>Our Services</h4><ul><li>Residential Roofing</li><li>Commercial Roofing</li><li>Roof Repairs &amp; Maintenance</li><li>Custom Roofing Solutions</li></ul></div>
<div class="f-col" style="left:807px"><h4>Signup for updates on design<br>ideas and latest trends</h4>
  <div class="newsletter"><span>hello@example.com</span><span style="color:var(--red)">➤</span></div>
  <p style="font-size:11px;margin-top:14px">*We don't spam</p>
</div>
<div class="abs totop">⌃</div>

</body>
</html>
```